Webdesign für vielseitiges Unternehmen
Zielgruppe
Die Seite wird HOCHMOOR-ART oder DESIGN heißen.
Das Unternehmen bietet folgende Segmente an:
1. Möbelstücke (meist Unikate, da restauriert mit eigener Kreation)
2. Fotografien
3. Malerei
4. Interieurdesign (Gestalten, Einrichten von Apartments, Häusern, Shops etc.) (hier muss natürlich mehr Platz für Informationstext sein.
5. Gallery. - Infos zu Öffnungszeiten und Bilder ebenfalls.
6. Die Location ist für Events buchbar
(7.) Blogg wenns nicht zu aufwändig ist. (hier möchte ich gern Bilder posten die ich irgendwo finde und als gut erachte. Oder Produkte. Wichtig ist, dass bei Verbreitung von Fremdpostings, immer die Quelle eingefügt werden muss. Am besten automatisch. Ich muss zu dem Post noch eigenes Kommentar abgeben können.
Für jedes Segment soll eine Unterseite geschaffen werden.
Die Produktfotos sollen clean aufgebaut sein. Am besten je Produkt 1 Bild pro Seite. Vielleicht erst nachdem man auf ein Bild in der Auswahl geklickt hat?? 3 nebeneinander und dann neue Zeile.
Unter den Bildern (hauptsächlich Querformat aber Hochformat muss auch gehen) müssen Angaben stehen:
-Art
-Size
-Auflage
-Preis
-liken für Social Media oder weiterleiten (wenn möglich)
-Fragen zu diesem Produkt ( wenn hier jemand klickt und etwas schreibt, muss ich eine mail erhalten, wo ich direkt ersehen kann, zu welchem Produkt die Frage zugeordnet ist.
Pro Artikel müssen mehrere Bilder eingestellt werden können, die der Client durch einfaches klicken durchklicken kann.
Die Seite soll clean, chic und Edel wirken. Hauptsächlich über Bilder. Shopsystem ist wegen Aufwandskosten erstmal nicht geplant)
Ich muss die Seite selber pflegen können, auch SEO Optimieren (ohne Programierkenntnisse)
Die Seite soll eine Seite für verschiedene Aspekte sein wie:
- Gallerie
hier wird die Gallerie vorgestellt und Bilder gezeigt von Ausstellungen und Künstlervorstellung..
Aufgabenstellung
Schwarz- Weiß
Akzente eventuell in Patinagrün oder Grünspan oder Malachitgrün oder Gold
Mobilgeräte responsiv

```html
<!DOCTYPE html>
<html lang="de">
<head>
<meta charset="utf-8">
<title>HOCHMOOR – Interieur · Design · Galerie</title>
<link rel="stylesheet" href="https://fonts.googleapis.com/css2?family=Source+Sans+3:wght@300;400;600&display=swap">
<style>
  :root {
    --page-bg: #f8f8f8;
    --panel-bg: #ffffff;
    --ink: #1e1e1e;
    --text: #2b2b2b;
    --muted: #a6a6a6;
    --nav: #9c9c9c;
    --accent: #4a7565;
    --field-border: #bdbdbd;
    --arrow-bg: rgba(220,220,220,0.85);
  }
  * { box-sizing: border-box; margin: 0; padding: 0; }
  html, body { width: 1200px; height: 1088px; overflow: hidden; }
  body {
    background: var(--page-bg);
    font-family: "Source Sans 3", "Helvetica Neue", Arial, sans-serif;
    color: var(--text);
    position: relative;
  }
  .site-header { height: 155px; position: relative; }
  .brand { position: absolute; top: 32px; left: 0; width: 100%; text-align: center; }
  .brand-name {
    font-size: 28px; font-weight: 600; letter-spacing: 2px; color: var(--ink); line-height: 1;
  }
  .brand-tagline {
    margin-top: 5px; font-size: 7.5px; letter-spacing: 2.6px; color: var(--ink); font-weight: 600;
  }
  .main-nav {
    position: absolute; top: 104px; left: 187px;
    display: flex; font-size: 15px; font-weight: 300; text-transform: uppercase;
  }
  .main-nav a { color: var(--nav); text-decoration: none; padding: 0 9px 4px; }
  .main-nav a.is-active { color: var(--accent); border-bottom: 1.5px solid var(--accent); }
  .hero {
    position: absolute; top: 155px; left: 0; width: 1200px; height: 723px;
    background: var(--panel-bg); box-shadow: 0 1px 2px rgba(0,0,0,0.08);
  }
  .hero-image {
    position: absolute; left: 2px; top: 0; width: 598px; height: 723px;
    background: linear-gradient(180deg, #efefed 0%, #e9e7e3 55%, #b99a78 82%, #8a6a4c 100%);
  }
  .slider-arrow {
    position: absolute; top: 335px; width: 53px; height: 53px; border-radius: 50%;
    background: var(--arrow-bg);
  }
  .slider-arrow svg { display: block; margin: 15px auto; }
  .slider-arrow.prev { left: 26px; }
  .slider-arrow.next { left: 1120px; }
  .hero-content { position: absolute; left: 702px; top: 92px; width: 450px; }
  .hero-title { font-size: 35px; font-weight: 300; color: var(--accent); line-height: 1.2; }
  .hero-text { margin-top: 22px; font-size: 14.8px; font-weight: 300; line-height: 28px; }
  .hero-text + .hero-text { margin-top: 28px; }
  .question-form { position: absolute; left: 701px; top: 555px; width: 428px; }
  .question-label { font-size: 12.5px; font-weight: 300; color: var(--nav); }
  .question-field { margin-top: 14px; position: relative; height: 39px; }
  .question-input {
    width: 100%; height: 39px; border: 1.5px solid var(--field-border); border-radius: 5px;
    padding-left: 13px; font-family: Arial, sans-serif; font-size: 12.5px; color: var(--muted);
    background: #fff; display: flex; align-items: center;
  }
  .question-send {
    position: absolute; right: 0; top: 0; width: 60px; height: 39px; border-radius: 5px;
    background: var(--accent); box-shadow: 0 4px 8px rgba(200,80,80,0.15);
  }
  .question-send svg { display: block; margin: 9px auto; }
  .social { position: absolute; left: 1058px; top: 669px; display: flex; gap: 14px; }
  .social span { width: 15px; height: 15px; border: 1.5px solid #333; border-radius: 50%; }
  .site-footer {
    position: absolute; top: 930px; left: 352px; display: flex;
    font-size: 15px; font-weight: 300; color: var(--muted);
  }
  .footer-col { list-style: none; line-height: 31px; }
  .footer-col:nth-child(1) { width: 184px; }
  .footer-col:nth-child(2) { width: 173px; }
</style>
</head>
<body>
  <header class="site-header">
    <div class="brand">
      <div class="brand-name">HOCHMOOR</div>
      <div class="brand-tagline">INTERIEUR · DESIGN · GALERIE</div>
    </div>
    <nav class="main-nav">
      <a class="is-active" href="#">Home</a>
      <a href="#" style="margin-left:8px">Über uns</a>
      <a href="#" style="margin-left:35px">Gallerie</a>
      <a href="#" style="margin-left:32px">Fotografie</a>
      <a href="#" style="margin-left:33px">Malerei</a>
      <a href="#" style="margin-left:33px">Interieur</a>
      <a href="#" style="margin-left:36px">Blog</a>
      <a href="#" style="margin-left:29px">Kontakt</a>
    </nav>
  </header>

  <section class="hero">
    <div class="hero-image" role="img" aria-label="Helles Schlafzimmer mit rundem Holzspiegel, weißer Kommode, großer Zimmerpflanze und Bett auf Holzboden"></div>
    <div class="slider-arrow prev"><svg width="22" height="22" viewBox="0 0 22 22"><path d="M14 3 L6 11 L14 19" fill="none" stroke="#fff" stroke-width="3.5" stroke-linecap="round"/></svg></div>
    <div class="slider-arrow next"><svg width="22" height="22" viewBox="0 0 22 22"><path d="M8 3 L16 11 L8 19" fill="none" stroke="#fff" stroke-width="3.5" stroke-linecap="round"/></svg></div>

    <div class="hero-content">
      <h1 class="hero-title">Willkommen bei HOCHMOOR</h1>
      <p class="hero-text">Lorem ipsum dolor sit amet, consetetur sadipscing elitr, sed diam nonumy eirmod tempor invidunt ut labore et dolore magna aliquyam erat, sed diam voluptua. At vero eos et accusam et justo duo dolores et ea rebum. Stet clita kasd gubergren, no sea takimata sanctus est Lorem ipsum dolor sit amet. Lorem ipsum dolor sit amet, consetetur sadipscing elitr, sed diam nonumy eirmod tempor invidunt ut labore et dolore magna aliquyam erat, sed diam voluptua.</p>
      <p class="hero-text">At vero eos et accusam et justo duo dolores et ea rebum. Stet clita kasd gubergren, no sea takimata sanctus est Lorem ipsum dolor sit amet.</p>
    </div>

    <form class="question-form">
      <p class="question-label">Stellen Sie uns eine Frage zu Kunstwerk 123, wir helfen Ihnen gerne weiter.</p>
      <div class="question-field">
        <div class="question-input">Ihre Frage</div>
        <div class="question-send"><svg width="22" height="20" viewBox="0 0 22 20"><path d="M2 2 L20 10 L2 18 L5 10 Z M5 10 H12" fill="none" stroke="#fff" stroke-width="1.6" stroke-linejoin="round"/></svg></div>
      </div>
    </form>

    <div class="social" aria-label="Soziale Netzwerke"><span></span><span></span><span></span></div>
  </section>

  <footer class="site-footer">
    <ul class="footer-col"><li>Über Uns</li><li>Blog</li><li>Datenschutz</li><li>Impressum</li></ul>
    <ul class="footer-col"><li>Gallerie</li><li>Fotografie</li><li>Malerei</li><li>Intereur</li></ul>
    <ul class="footer-col"><li>Moorweg 12a</li><li>12345 Musterstadt</li><li>T. +49 000 555 0142</li><li>info@hochmoor-art.de</li></ul>
  </footer>
</body>
</html>
```